Wordpress Design Project

The aim of our website is to provide information to a target market of people aged 17 - 22. We need the site to be appealing and also functional that contains a log in and possible forum so people can upload images and ideas. We have broken the information down into four categories and are looking for a website design somewhat like the following. Keeping in mind we are open to feedback from you and also ideas.

Website:
we need a word press design that contains the following:

- 1 main title page that contains a logo at the top centre and 4 main links with the mouse over function.

- all of the four links would then forward you to seperate pages that contain a slide bar at the top which enables the user to view different options. Once the user clicks on the option information will be provided below the scroll system. As well as the information we are looking to have a visual beside it, so a clipnest video beside it.

Target Market(s)

17 - 22 year olds

Industry/Entity Type

Clipnest

Requirements
Nice to have
• Forum and login

```html
<!DOCTYPE html>
<html lang="en">
<head>
<meta charset="utf-8">
<title>Next Chapter Hub</title>
<link href="https://fonts.googleapis.com/css2?family=Questrial&family=Arimo:wght@400;700&family=Great+Vibes&display=swap" rel="stylesheet">
<style>
  :root {
    --blue: #1e9ad0;
    --orange: #f0a040;
    --orange-dark: #f0921e;
    --login: #f06020;
    --grey-band: #e8e8e8;
    --text-grey: #8a8a8a;
    --nav-grey: #8c8c8c;
    --dark: #555;
    --white: #fff;
  }
  * { margin: 0; padding: 0; box-sizing: border-box; }
  html, body { width: 1200px; height: 806px; overflow: hidden; background: var(--white); }
  body { position: relative; font-family: "Arimo", Arial, sans-serif; }

  .site-header { position: absolute; left: 0; top: 0; width: 1200px; height: 80px; border-bottom: 1px dashed #cfcfcf; }
  .brand { position: absolute; left: 200px; top: 18px; font-family: "Questrial", sans-serif; font-size: 34px; color: var(--blue); letter-spacing: -0.5px; }
  .brand-mark { display: inline-block; width: 14px; height: 14px; border-radius: 50%; background: var(--orange-dark); margin-right: 8px; vertical-align: 4px; }

  .main-nav { position: absolute; left: 517px; top: 27px; display: flex; align-items: center; font-size: 13px; }
  .main-nav a { color: var(--nav-grey); text-decoration: none; }
  .main-nav .active { background: var(--blue); color: var(--white); font-weight: 700; width: 62px; height: 23px; line-height: 23px; text-align: center; margin-right: 17px; }
  .main-nav .sep { width: 1px; height: 10px; border-left: 1px dotted #999; margin: 0 16px; }

  .account { position: absolute; left: 891px; top: 28px; display: flex; gap: 3px; }
  .account a { height: 21px; line-height: 21px; font-size: 11px; color: var(--white); text-decoration: none; text-align: center; border-radius: 2px; }
  .forum { background: var(--blue); width: 54px; }
  .login { background: var(--login); width: 54px; }

  .hero { position: absolute; left: 280px; top: 84px; width: 640px; height: 394px; background: linear-gradient(90deg, #c9a07a 0%, #e8e0d8 25%, #7cc7e8 50%, #5a88c8 75%, #cfd8e4 100%); }
  .hero-rule { position: absolute; left: 200px; top: 478px; width: 800px; height: 6px; }

  .signup { position: absolute; left: 262px; top: 500px; width: 680px; height: 44px; }
  .signup-title { position: absolute; left: 0; top: 0; font-family: "Great Vibes", cursive; font-size: 32px; color: var(--blue); }
  .signup-input { position: absolute; left: 198px; top: 5px; width: 344px; height: 34px; border: 1px solid #bbb; padding-left: 7px; font-size: 10px; color: #888; line-height: 32px; box-shadow: inset 0 1px 2px rgba(0,0,0,.12); }
  .signup-button { position: absolute; left: 551px; top: 5px; width: 125px; height: 34px; background: var(--orange); color: var(--white); font-family: "Questrial", sans-serif; font-size: 20px; text-align: center; line-height: 34px; }

  .content-band { position: absolute; left: 0; top: 558px; width: 1200px; height: 248px; background: var(--grey-band); }
  .categories { position: absolute; left: 200px; top: 0; display: flex; gap: 16px; }
  .categories a { width: 188px; height: 45px; background: var(--blue); color: var(--white); font-family: "Questrial", sans-serif; font-size: 28px; text-align: center; line-height: 45px; text-decoration: none; }

  .welcome { position: absolute; left: 200px; top: 62px; width: 820px; }
  .welcome h1 { font-family: "Questrial", sans-serif; font-weight: 700; font-size: 30px; color: var(--orange-dark); margin-bottom: 6px; }
  .welcome p { font-size: 9.6px; line-height: 13.6px; color: var(--text-grey); }

  .footer-rule { position: absolute; left: 200px; top: 191px; width: 800px; height: 3px; }
  .footer-nav { position: absolute; left: 201px; top: 206px; display: flex; align-items: center; font-size: 10.5px; font-weight: 700; }
  .footer-nav a { color: #666; text-decoration: none; }
  .footer-nav .sep { height: 9px; border-left: 1px dotted #888; margin: 0 12px; }
  .copyright { position: absolute; left: 201px; top: 222px; font-size: 9.6px; color: var(--text-grey); }

  .social { position: absolute; left: 892px; top: 207px; display: flex; gap: 4px; }
  .social span { width: 24px; height: 24px; border-radius: 50%; background: #555; color: var(--white); font-size: 11px; font-weight: 700; text-align: center; line-height: 24px; }
</style>
</head>
<body>
  <header class="site-header">
    <div class="brand"><span class="brand-mark"></span>Next Chapter Hub</div>
    <nav class="main-nav">
      <a class="active" href="#">Home</a>
      <a href="#">About Us</a><span class="sep"></span>
      <a href="#">Services</a><span class="sep"></span>
      <a href="#">Contact Us</a>
    </nav>
    <div class="account">
      <a class="forum" href="#">Forum</a>
      <a class="login" href="#">Login &#9662;</a>
    </div>
  </header>

  <div class="hero" role="img" aria-label="Group photo of five smiling young people in colourful casual clothes"></div>
  <svg class="hero-rule" viewBox="0 0 800 6" preserveAspectRatio="none">
    <defs><linearGradient id="rule" x1="0" x2="1"><stop offset="0" stop-color="#ccc" stop-opacity="0"/><stop offset=".5" stop-color="#999"/><stop offset="1" stop-color="#ccc" stop-opacity="0"/></linearGradient></defs>
    <path d="M0 1 Q400 6 800 1 Q400 3 0 1Z" fill="url(#rule)"/>
  </svg>

  <section class="signup">
    <div class="signup-title">Get Information</div>
    <div class="signup-input">Enter your email</div>
    <div class="signup-button">Subscribe</div>
  </section>

  <main class="content-band">
    <nav class="categories">
      <a href="#">Gap year</a>
      <a href="#">Schoolies</a>
      <a href="#">University</a>
      <a href="#">Trades</a>
    </nav>
    <section class="welcome">
      <h1>Welcome:</h1>
      <p>Lorem ipsum dolor sit amet, consectetur adipiscing elit. Cras ut mi sit amet dolor mattis aliquet. Cras consequat adipiscing mattis. In sit amet arcu iaculis, tristique mauris non, hendrerit urna. Mauris condimentum faucibus varius. Quisque at sapien eleifend, sagittis erat nec, gravida leo. Sed dictum ipsum vitae lectus pulvinar ultricies. Vivamus scelerisque neque eu erat ultricies elementum.</p>
      <p>Morbi vestibulum lectus sit amet elit molestie, quis egestas ligula vulputate. Vestibulum sit amet accumsan lectus. Nulla et erat consectetur, imperdiet mi vel, ultrices ipsum. Duis odio est, posuere et sapien quis, sollicitudin accumsan mauris. Suspendisse eleifend</p>
    </section>
    <svg class="footer-rule" viewBox="0 0 800 3" preserveAspectRatio="none">
      <path d="M0 1.5 Q400 0 800 1.5" stroke="#aaa" stroke-width="1.2" fill="none"/>
    </svg>
    <nav class="footer-nav">
      <a href="#">Home</a><span class="sep"></span>
      <a href="#">About Us</a><span class="sep"></span>
      <a href="#">Services</a><span class="sep"></span>
      <a href="#">Contact Us</a>
    </nav>
    <p class="copyright">Copyright © 2012-2013 NextChapterHub &nbsp;| All Rights Reserved &nbsp;| &nbsp;Privacy Policy</p>
    <div class="social" aria-label="Social links: Linkwall, Peeploop, Postpad, Clipnest">
      <span>L</span><span>P</span><span>P</span><span>C</span>
    </div>
  </main>
</body>
</html>
```